Bright Smile Dental*

Promotion for a new dental office
brghtsmlvoranta.com

I just opened a new dental office and would like to promote my office to
the public. I attached some examples. I have AI files for logo and also can
provide office pictures. Website is brightsmilevoranta.com.

Target Market(s)

General public

Requirements
Must have
• Dr. Tovin
• Halvern State, BS, MCB
• Marwick School of Dentistry
• US Army veteran
• New patient exam, X-rays and basic cleaning for $95.
• White background
• 20% discount with this post card. This only applied to private pay patients(in fine print)
• Open saturdays and evenings
Should not have
• No postal info. Not going to mail this out.

```html
<!DOCTYPE html>
<html lang="en">
<head>
<meta charset="utf-8">
<title>Bright Smile Dental – New Patient Offer</title>
<link rel="stylesheet" href="https://fonts.googleapis.com/css2?family=Arvo:ital,wght@0,400;1,700&family=Montserrat:wght@300&family=Source+Sans+3:wght@400&family=Oswald:wght@500;600&family=Lato:wght@400;700&display=swap">
<style>
  :root {
    --ink: #4a4a4c;
    --ink-soft: #555759;
    --brand-blue: #0f5596;
    --deep-blue: #0b4f86;
    --band-grey: #3c3c3e;
    --bar-grey: #454547;
    --leaf-green: #8cc152;
    --paper: #ffffff;
    --paper-shade: #e9e9ea;
    --icon-blue: #1e88c9;
    --icon-navy: #3d5a98;
  }
  * { margin: 0; padding: 0; box-sizing: border-box; }
  html, body { width: 1200px; height: 816px; overflow: hidden; background: var(--paper); }
  .postcard {
    position: relative; width: 1200px; height: 816px; overflow: hidden;
    background: radial-gradient(ellipse at 40% 40%, var(--paper) 0%, #f4f4f5 55%, var(--paper-shade) 100%);
  }
  .brand { position: absolute; left: 78px; top: 74px; display: flex; align-items: center; }
  .brand-mark { width: 104px; height: 104px; border: 2px solid var(--ink); border-radius: 50%; margin-right: 14px; flex: none; }
  .brand-name { font-family: "Montserrat", sans-serif; font-weight: 300; font-size: 33px; letter-spacing: 0.5px; color: var(--ink); line-height: 1; white-space: nowrap; }
  .brand-tagline { font-family: "Source Sans 3", sans-serif; font-size: 25px; letter-spacing: 0.3px; color: var(--ink); margin-top: 10px; padding-left: 2px; white-space: nowrap; }
  .family-photo {
    position: absolute; left: 70px; top: 184px; width: 570px; height: 560px;
    background: linear-gradient(160deg, #e4d6c8 0%, #d9c2ae 35%, #c6d4e4 65%, #9fb3cc 100%);
    border-radius: 40% 40% 0 0 / 22% 22% 0 0;
  }
  .offer { position: absolute; left: 644px; top: 78px; width: 480px; text-align: center; }
  .offer-intro { font-family: "Arvo", serif; font-size: 42px; color: var(--ink); line-height: 1.2; white-space: nowrap; }
  .offer-headline {
    font-family: "Arvo", serif; font-style: italic; font-weight: 700; font-size: 66px;
    color: var(--brand-blue); line-height: 1.05; letter-spacing: 1px; white-space: nowrap;
    text-shadow: 2px 2px 0 var(--paper), 3px 3px 3px rgba(0,0,0,0.25);
  }
  .coupon { position: absolute; left: 664px; top: 272px; width: 440px; }
  .coupon-price {
    height: 110px; background: var(--paper); border: 2px dashed #8a8a8c; border-bottom: none;
    border-radius: 8px 8px 0 0; display: flex; align-items: center; justify-content: center; gap: 14px;
  }
  .price { font-family: "Oswald", sans-serif; font-weight: 600; font-size: 80px; color: var(--brand-blue); line-height: 1; }
  .price-label { font-family: "Oswald", sans-serif; font-weight: 600; font-size: 50px; color: #333335; line-height: 1; margin-top: 10px; }
  .coupon-detail {
    height: 50px; background: var(--bar-grey); border-radius: 0 0 10px 10px;
    font-family: "Oswald", sans-serif; font-weight: 500; font-size: 21px; color: var(--paper);
    display: flex; align-items: center; justify-content: center; white-space: nowrap;
  }
  .dentist { position: absolute; left: 644px; top: 444px; width: 480px; text-align: center; font-family: "Lato", sans-serif; }
  .dentist-name { font-weight: 700; font-size: 40px; color: var(--brand-blue); line-height: 1.1; }
  .dentist-credentials { list-style: none; font-size: 26px; color: var(--ink-soft); line-height: 32px; margin-top: 2px; }
  .waves { position: absolute; left: 0; top: 0; }
  .visit { position: absolute; left: 646px; top: 726px; font-family: "Lato", sans-serif; color: var(--paper); line-height: 1.2; }
  .visit-hours { font-weight: 700; font-size: 20px; }
  .visit-web { font-size: 17px; }
  .fine-print { position: absolute; left: 300px; top: 792px; font-family: "Lato", sans-serif; font-size: 12px; color: #dbe6f1; white-space: nowrap; }
</style>
</head>
<body>
<main class="postcard">
  <div class="family-photo" role="img" aria-label="Smiling family of four hugging on a white sofa"></div>

  <svg class="waves" width="1200" height="816" viewBox="0 0 1200 816" aria-hidden="true">
    <path fill="var(--leaf-green)" d="M560,700 C760,640 1000,600 1200,612 L1200,664 C1000,652 800,672 560,722 Z"/>
    <path fill="var(--band-grey)" d="M0,600 C120,700 300,735 560,722 C800,690 1000,662 1200,662 L1200,816 L0,816 Z"/>
    <path fill="var(--deep-blue)" d="M0,816 L0,770 C200,782 400,748 600,728 C850,696 1050,676 1200,676 L1200,816 Z"/>
    <circle cx="992" cy="734" r="19" fill="var(--icon-blue)"/>
    <circle cx="1033" cy="734" r="19" fill="var(--icon-navy)"/>
    <circle cx="1077" cy="734" r="19" fill="var(--icon-blue)"/>
  </svg>

  <header class="brand">
    <div class="brand-mark"></div>
    <div>
      <div class="brand-name">BRIGHT SMILE DENTAL</div>
      <div class="brand-tagline">MODERN GENERAL DENTISTRY</div>
    </div>
  </header>

  <section class="offer">
    <p class="offer-intro">We are welcoming</p>
    <p class="offer-headline">new patients</p>
    <p class="offer-intro">with a special offer</p>
  </section>

  <section class="coupon">
    <div class="coupon-price">
      <span class="price">$95</span>
      <span class="price-label">FULL CHECKUP</span>
    </div>
    <div class="coupon-detail">NEW PATIENT EXAM, X-RAYS AND BASIC CLEANING</div>
  </section>

  <section class="dentist">
    <h2 class="dentist-name">Dr. Tovin</h2>
    <ul class="dentist-credentials">
      <li>Halvern State, BS, MCB</li>
      <li>Marwick School of Dentistry</li>
      <li>US Army veteran</li>
    </ul>
  </section>

  <footer>
    <div class="visit">
      <p class="visit-hours">Open Saturdays &amp; Evenings</p>
      <p class="visit-web">brightsmilevoranta.com</p>
    </div>
    <p class="fine-print">*20% discount with this postcard. Applies to private pay patients only.</p>
  </footer>
</main>
</body>
</html>
```